NEW Gym Timetable for Muay Thai gym!

We need a new timetable for our Muay Thai gym - the times, classes and logos are attached. Our primary logo font is MACHINE BT

The gym is called Kroval Fit. The address is Level 2, 58-60 Brindlemere Road, Tallowdene, Canberra

We are open Monday to Saturday and Sunday by appointment.

Our website and more information can be found at www.kroval.com.au.

Please message me for more information/feedback

```html
<!DOCTYPE html>
<html lang="en">
<head>
<meta charset="utf-8">
<title>Kroval Fit Timetable</title>
<link href="https://fonts.googleapis.com/css2?family=Anton&family=Oswald:wght@500&family=Open+Sans:wght@400;600;700&display=swap" rel="stylesheet">
<style>
:root{
  --green:#0e7a3b;
  --green-dark:#0a5c2c;
  --green-light:#1aa152;
  --grey-text:#555b60;
  --cell-top:#ffffff;
  --cell-bottom:#dcdfe1;
  --line:#c9cdd0;
  --page:#e8e8e8;
}
*{margin:0;padding:0;box-sizing:border-box}
html,body{width:830px;height:1200px;overflow:hidden;background:var(--page)}
.poster{
  position:absolute;left:20px;top:321px;width:790px;height:558px;overflow:hidden;
  font-family:"Open Sans",sans-serif;box-shadow:0 4px 14px rgba(0,0,0,.25);
}
.poster-photo{
  position:absolute;inset:0;
  background:
    linear-gradient(to bottom,rgba(0,0,0,0) 55%,rgba(20,22,24,.55) 100%),
    linear-gradient(to right,#7d868d 0%,#a7aeb2 30%,#8b9195 55%,#3a3e42 75%,#1c1e21 100%);
}
.brand-tab{
  position:absolute;left:22px;top:0;width:142px;height:134px;
}
.brand-tab svg{position:absolute;inset:0}
.brand-name{
  position:absolute;left:0;right:0;top:44px;text-align:center;
  font-family:"Oswald",sans-serif;font-weight:500;font-size:25px;color:var(--green);letter-spacing:1px;
}
.headline{
  position:absolute;left:197px;width:395px;top:14px;text-align:center;
  font-family:"Anton",sans-serif;font-size:66px;line-height:1;color:var(--green);letter-spacing:2px;
}
.subline{
  position:absolute;left:197px;width:395px;text-align:center;
  font-family:"Oswald",sans-serif;font-weight:500;color:#6a6f73;letter-spacing:.5px;
}
.subline.days{top:88px;font-size:24px}
.subline.appt{top:121px;font-size:22px}
.timetable{
  position:absolute;left:93px;top:295px;width:605px;
  display:grid;grid-template-columns:repeat(7,1fr);grid-template-rows:29px 45px 38px 39px 38px;
}
.day{
  background:var(--green);color:#fff;font-weight:700;font-size:12.5px;
  display:flex;align-items:center;justify-content:center;border-right:1px solid var(--green-dark);
}
.slot{
  background:linear-gradient(to bottom,var(--cell-top),var(--cell-bottom));
  border-right:1px solid var(--line);border-bottom:1px solid var(--line);
  display:flex;flex-direction:column;align-items:center;justify-content:center;text-align:center;
  padding:0 2px;
}
.slot .time{color:var(--green);font-weight:700;font-size:7.6px;line-height:1.3}
.slot .class{color:var(--grey-text);font-size:6.6px;line-height:1.45}
.info-bar{
  position:absolute;left:136px;top:496px;width:533px;height:24px;border-radius:4px;
  background:linear-gradient(to bottom,var(--green-light),var(--green));
  display:flex;align-items:center;justify-content:center;gap:10px;color:#fff;font-size:11px;
}
.info-bar .divider{width:1px;height:13px;background:rgba(255,255,255,.7)}
.info-bar .item{display:flex;align-items:center;gap:5px}
.info-bar b{font-weight:700}
.social{
  position:absolute;top:526px;left:0;right:0;display:flex;justify-content:center;gap:4px;
}
.social span{width:24px;height:24px;border-radius:50%;background:var(--green);border:2px solid #fff}
</style>
</head>
<body>
<div class="poster">
  <div class="poster-photo" role="img" aria-label="Photo of a trainer coaching a woman in a gym, blurred gym equipment in the background"></div>

  <div class="brand-tab">
    <svg width="142" height="134" viewBox="0 0 142 134">
      <defs><linearGradient id="tabFill" x1="0" y1="0" x2="0" y2="1"><stop offset="0" stop-color="#ffffff"/><stop offset="1" stop-color="#d6d9db"/></linearGradient></defs>
      <path d="M2 0 H140 V106 L71 132 L2 106 Z" fill="url(#tabFill)" stroke="#0e7a3b" stroke-width="1.5"/>
    </svg>
    <div class="brand-name">Kroval Fit</div>
  </div>

  <div class="headline">WE ARE OPEN</div>
  <div class="subline days">MONDAY TO SATURDAY AND SUNDAY</div>
  <div class="subline appt">BY APPOINTMENT</div>

  <div class="timetable">
    <div class="day">Monday</div><div class="day">Tuesday</div><div class="day">Wednesday</div><div class="day">Thursday</div><div class="day">Friday</div><div class="day">Saturday</div><div class="day">Sunday</div>

    <div class="slot"><span class="time">6.00AM — 7:00AM</span><span class="class">Clinching</span><span class="class">(Fighters/By invitation)</span></div>
    <div class="slot"><span class="time">6:00AM—6:45AM</span><span class="class">Muay HiiT</span></div>
    <div class="slot"><span class="time">6.00AM — 7:00AM</span><span class="class">Clinching</span><span class="class">(Fighters/By invitation)</span></div>
    <div class="slot"><span class="time">6:00AM—6:45AM</span><span class="class">Muay HiiT</span></div>
    <div class="slot"></div>
    <div class="slot"><span class="time">8.00AM —8:45AM</span><span class="class">Muay HiiT</span><span class="class">(Fighters/By invitation)</span></div>
    <div class="slot"></div>

    <div class="slot"><span class="time">5:30PM — 6:30PM</span><span class="class">Muay Thai</span></div>
    <div class="slot"><span class="time">5:30PM— 6:30PM</span><span class="class">Boxing</span></div>
    <div class="slot"><span class="time">5:30PM — 6:30PM</span><span class="class">Muay Thai</span></div>
    <div class="slot"><span class="time">5:30PM— 6:30PM</span><span class="class">Boxing</span></div>
    <div class="slot"><span class="time">5:30PM —7:00 PM</span><span class="class">Muay Thai Weekly wrap</span></div>
    <div class="slot"><span class="time">9:00AM—11:00AM</span><span class="class">Sparring</span></div>
    <div class="slot"><span class="class">Personal Training</span><span class="class">By Appointment</span></div>

    <div class="slot"><span class="time">6:30PM — 7:30PM</span><span class="class">Padwork &amp; Bagwork</span></div>
    <div class="slot"><span class="time">6:30PM — 7:30PM</span><span class="class">Muay Thai</span></div>
    <div class="slot"><span class="time">6:30PM — 7:30PM</span><span class="class">Padwork &amp; Bagwork</span></div>
    <div class="slot"><span class="time">6:30PM — 7:30PM</span><span class="class">Muay Thai</span></div>
    <div class="slot"></div>
    <div class="slot"><span class="time">12:00PM — 1:00PM</span><span class="class">Muay Thai</span></div>
    <div class="slot"></div>

    <div class="slot"><span class="time">7:30 PM — 8:30 PM</span><span class="class">Fighters</span></div>
    <div class="slot"><span class="time">6:30 PM — 8:30 PM</span><span class="class">Fighters</span></div>
    <div class="slot"><span class="time">7:30 PM — 8:30 PM</span><span class="class">Fighters</span></div>
    <div class="slot"><span class="time">6:30 PM — 8:30 PM</span><span class="class">Fighters</span></div>
    <div class="slot"></div>
    <div class="slot"></div>
    <div class="slot"></div>
  </div>

  <div class="info-bar">
    <span class="item">
      <svg width="10" height="12" viewBox="0 0 10 12"><path d="M5 0.5a4 4 0 0 1 4 4c0 3-4 7-4 7s-4-4-4-7a4 4 0 0 1 4-4z" fill="none" stroke="#fff" stroke-width="1.2"/><circle cx="5" cy="4.5" r="1.4" fill="#fff"/></svg>
      Level 2, 58-60 Brindlemere Road, Tallowdene, Canberra
    </span>
    <span class="divider"></span>
    <span class="item">
      <svg width="11" height="11" viewBox="0 0 11 11"><circle cx="5.5" cy="5.5" r="4.8" fill="none" stroke="#fff" stroke-width="1"/><ellipse cx="5.5" cy="5.5" rx="2" ry="4.8" fill="none" stroke="#fff" stroke-width=".8"/><line x1=".7" y1="5.5" x2="10.3" y2="5.5" stroke="#fff" stroke-width=".8"/></svg>
      www.<b>kroval</b>.com.au
    </span>
  </div>

  <div class="social"><span></span><span></span><span></span></div>
</div>
</body>
</html>
```